Kestra Rowe - Contact/Landing Page

I need a landing page which will essentially be the page that customers will go to from the 'website' link on TLX listing. It will provide a short overview of services which need to be selectable. a little further down can capture some contact details followed by a large Submit Now button etc...

I have some icon/logo's that can be utilised at the bottom of the page as industry type references.

Target Market(s)

End of Lease Cleaning Services

Industry/Entity Type

Cleaning Service

Colors

Designer to choose colors to be used in the design.

Requirements
Must have
• As per description
Should not have
• Colours to match my website kestrarowe.com.au

```html
<!DOCTYPE html>
<html lang="en">
<head>
<meta charset="utf-8">
<title>Kestra Rowe – End of Lease Cleaning & Licensed Pest Control</title>
<link rel="stylesheet" href="https://fonts.googleapis.com/css2?family=Poppins:wght@300;400;600;700&family=Roboto:wght@300;400;500;700&display=swap">
<style>
:root{
  --hero-blue:#1779c0;
  --contact-blue:#1668ad;
  --button-blue:#2d6ec0;
  --card-grey:#e6e6e6;
  --footer-grey:#ececec;
  --ink:#222;
  --muted:#666;
  --white:#fff;
}
*{box-sizing:border-box;margin:0;padding:0}
html,body{width:1200px;height:2427px;overflow:hidden;background:var(--white);font-family:'Roboto',sans-serif;color:var(--ink)}
.page{position:relative;width:1200px;height:2427px}

.hero{position:absolute;left:0;top:0;width:1200px;height:676px;background:var(--hero-blue)}
.hero-glow{position:absolute;left:420px;top:90px;width:360px;height:380px;border-radius:50%;background:radial-gradient(circle,rgba(255,255,255,.55) 0%,rgba(255,255,255,.15) 50%,rgba(255,255,255,0) 72%)}
.brand{position:absolute;left:0;top:245px;width:1200px;display:flex;align-items:center;justify-content:center;gap:18px}
.brand-dot{width:40px;height:40px;border-radius:50%;background:var(--white)}
.brand-name{font-family:'Poppins',sans-serif;font-weight:700;font-size:56px;color:var(--white);letter-spacing:1px}
.tagline{position:absolute;left:0;top:502px;width:1200px;text-align:center;font-size:44px;color:var(--white);font-weight:400}

.service{position:absolute;top:781px;width:313px;height:445px;background:var(--card-grey);text-align:center}
.service.featured{border:3px solid var(--button-blue);box-shadow:0 10px 14px rgba(0,0,0,.25);top:779px;height:450px;width:317px}
.service-photo{position:absolute;left:8px;top:8px;width:297px;height:187px}
.service.featured .service-photo{left:7px;top:7px}
.service-title{position:absolute;left:0;top:218px;width:100%;font-family:'Poppins',sans-serif;font-size:21px;line-height:26px;font-weight:400;color:var(--ink)}
.service-text{position:absolute;left:20px;top:285px;width:calc(100% - 40px);font-size:14px;line-height:26px;font-weight:300;color:var(--muted)}
.select-btn{position:absolute;left:51px;top:373px;width:211px;height:47px;border-radius:24px;background:var(--button-blue);color:var(--white);font-size:14px;font-weight:700;display:flex;align-items:center;padding-left:30px}
.select-btn .plus{position:absolute;right:2px;top:2px;width:43px;height:43px;border-radius:50%;background:var(--white);color:var(--button-blue);font-size:20px;display:flex;align-items:center;justify-content:center}

.contact{position:absolute;left:0;top:1321px;width:1200px;height:483px;background:var(--contact-blue)}
.contact-texture{position:absolute;inset:0;background:linear-gradient(135deg,rgba(0,0,0,.08),rgba(255,255,255,.04) 50%,rgba(0,0,0,.08))}
.contact-title{position:absolute;left:0;top:87px;width:1200px;text-align:center;font-size:34px;color:var(--white);font-weight:400}
.field{position:absolute;height:47px;background:var(--white);font-size:14px;color:#666;padding-left:16px;display:flex;align-items:center}
.submit{position:absolute;left:525px;top:344px;width:151px;height:47px;border:2px solid var(--white);color:var(--white);font-size:14px;font-weight:700;display:flex;align-items:center;justify-content:center}

.partner{position:absolute;top:1898px;width:231px;height:112px;background:var(--white);box-shadow:0 1px 6px rgba(0,0,0,.12);display:flex;align-items:center;justify-content:center}
.partner .badge{border-radius:6px}
.arrow{position:absolute;top:1940px}

.footer{position:absolute;left:0;top:2105px;width:1200px;height:322px;background:var(--footer-grey);font-family:'Poppins',sans-serif}
.footer h3{position:absolute;top:77px;font-size:20px;font-weight:700;color:#222}
.footer p{font-size:14px;line-height:17px;color:#555;font-weight:400}
.about{position:absolute;left:111px;top:127px;width:290px}
.info-row{position:absolute;left:505px;display:flex;gap:10px;align-items:flex-start}
.info-icon{width:36px;height:36px;border-radius:50%;background:var(--button-blue);display:flex;align-items:center;justify-content:center;flex:none}
.hours{position:absolute;left:893px;top:127px}
.pill{position:absolute;left:894px;width:166px;height:49px;border-radius:25px;font-size:14px;font-weight:600;display:flex;align-items:center;justify-content:center}
.pill.light{top:149px;background:var(--white);color:#222}
.pill.dark{top:209px;background:var(--button-blue);color:var(--white)}
.copyright{position:absolute;left:109px;top:247px;font-size:15px;color:#444}
</style>
</head>
<body>
<div class="page">

  <header class="hero">
    <div class="hero-glow"></div>
    <div class="brand"><span class="brand-dot"></span><span class="brand-name">Kestra Rowe</span></div>
    <h1 class="tagline">End of&nbsp; Lease Cleaning | Licensed Pest Control</h1>
  </header>

  <article class="service" style="left:111px">
    <div class="service-photo" role="img" aria-label="Cleaner vacuuming a bright living room" style="background:linear-gradient(135deg,#eceae6,#cfd3d2 60%,#9fb0ad)"></div>
    <h2 class="service-title">House &amp; End of<br>Lease Cleaning</h2>
    <p class="service-text">Moving house or is your lease ending? Presenting your property and getting your bond back has never been easier.</p>
    <div class="select-btn">SELECT<span class="plus">+</span></div>
  </article>

  <article class="service featured" style="left:441px">
    <div class="service-photo" role="img" aria-label="Cleaner wiping an office desk" style="background:linear-gradient(135deg,#d9d9d6,#f2f2f0 50%,#b9bdc0)"></div>
    <h2 class="service-title">Carpet Cleaning</h2>
    <p class="service-text">Our carpet cleaning service is of the highest quality and are undertaken in a multi-stage process done as per Australian Standards</p>
    <div class="select-btn">SELECT<span class="plus">+</span></div>
  </article>

  <article class="service" style="left:776px">
    <div class="service-photo" role="img" aria-label="Technician in protective suit spraying for pests" style="background:linear-gradient(135deg,#f4f6f7,#e3e6e8 60%,#c9ced1)"></div>
    <h2 class="service-title">Pest Control</h2>
    <p class="service-text">We are licensed and equipped to offer a full range of pest control services to the residential and commercial market</p>
    <div class="select-btn">SELECT<span class="plus">+</span></div>
  </article>

  <section class="contact">
    <div class="contact-texture" role="img" aria-label="Blue hexagon tile texture"></div>
    <h2 class="contact-title">CONTACT US</h2>
    <div class="field" style="left:283px;top:156px;width:308px">First name</div>
    <div class="field" style="left:609px;top:156px;width:308px">Sur name</div>
    <div class="field" style="left:283px;top:217px;width:308px">Email address</div>
    <div class="field" style="left:609px;top:217px;width:308px">Phone</div>
    <div class="field" style="left:283px;top:280px;width:634px">Subarb</div>
    <div class="submit">SUBMIT</div>
  </section>

  <svg class="arrow" style="left:42px" width="20" height="30" viewBox="0 0 20 30"><path d="M15 3 L4 15 L15 27" fill="none" stroke="#555" stroke-width="2.5"/></svg>
  <div class="partner" style="left:111px"><div class="badge" style="width:195px;height:80px;background:#111"></div></div>
  <div class="partner" style="left:360px"><div class="badge" style="width:160px;height:44px;background:#d9dcec"></div></div>
  <div class="partner" style="left:609px"><div class="badge" style="width:145px;height:86px;background:#cfd6ea"></div></div>
  <div class="partner" style="left:858px;background:#8db743"></div>
  <svg class="arrow" style="left:1132px" width="20" height="30" viewBox="0 0 20 30"><path d="M5 3 L16 15 L5 27" fill="none" stroke="#555" stroke-width="2.5"/></svg>

  <footer class="footer">
    <h3 style="left:111px">READY TO GET STARTED?</h3>
    <p class="about">Lorem ipsum dolor sit amet, consectetur adipiscing elit, sed do eiusmod tempor incididunt ut labore et dolore magna aliqua. Ut enim ad minim veniam, quis nostrud exercitation</p>

    <h3 style="left:505px">CONTACT US</h3>
    <div class="info-row" style="top:125px">
      <span class="info-icon"><svg width="12" height="16" viewBox="0 0 12 16"><path d="M6 0C2.7 0 0 2.6 0 5.9 0 10 6 16 6 16s6-6 6-10.1C12 2.6 9.3 0 6 0zm0 8a2 2 0 110-4 2 2 0 010 4z" fill="#fff"/></svg></span>
      <p style="width:270px">123,Lorem ipsum dolor sit consectetur adipiscing</p>
    </div>
    <div class="info-row" style="top:187px">
      <span class="info-icon"><svg width="14" height="14" viewBox="0 0 24 24"><path d="M6.6 10.8a15 15 0 006.6 6.6l2.2-2.2a1 1 0 011-.25 11.4 11.4 0 003.6.6 1 1 0 011 1V20a1 1 0 01-1 1A17 17 0 013 4a1 1 0 011-1h3.5a1 1 0 011 1c0 1.25.2 2.45.57 3.57a1 1 0 01-.25 1z" fill="#fff"/></svg></span>
      <p style="padding-top:8px">+1 888 888 8888</p>
    </div>

    <h3 style="left:891px">HOURS</h3>
    <p class="hours">Mon-Sat, 8AM – 8PM</p>
    <div class="pill light">GET IN TOUCH</div>
    <div class="pill dark">OUR WORK</div>

    <div class="copyright">©&nbsp; Copyrights 2021 Company name | All Rights Reserved</div>
  </footer>

</div>
</body>
</html>
```